Business card design needed

We need a business card for a consulting company called Harbor Business Consulting which covers a range of business services in construction and Human Resources. We have chosen balck and red as the colours and have an idea for the logo of a person with arms outstretched signifying all encompassing. See attachment.
Industry/Entity Type
Construction
Contact Information for Business Card
Dennis Holloway
Business Consultant/Project Manager/ Experienced Builder (Dip Bdg & Construction)
Mobile: 0481 362 954
Email: dennisholloway@harborconsulting.com.au
PO Box 7814
Kelvin Heights, QLD, 4172, Australia
Logo Text
Harbor Business Consulting
Look and feel

```html
<!DOCTYPE html>
<html lang="en">
<head>
<meta charset="utf-8">
<title>Harbor Business Consulting – Business Card</title>
<link rel="stylesheet" href="https://fonts.googleapis.com/css2?family=Roboto+Condensed:wght@400;700&display=swap">
<style>
  :root {
    --page: #ebeced;
    --card: #ffffff;
    --ink: #111111;
    --charcoal: #2a2a2a;
    --red: #e30613;
    --shadow: rgba(0,0,0,0.28);
  }
  * { margin: 0; padding: 0; box-sizing: border-box; }
  html, body { width: 1200px; height: 419px; overflow: hidden; background: var(--page); }
  body { position: relative; font-family: "Roboto Condensed", "Arial Narrow", sans-serif; color: var(--ink); }

  .card {
    position: absolute;
    width: 533px; height: 307px;
    background: var(--card);
    box-shadow: 0 6px 10px var(--shadow);
    overflow: hidden;
  }
  .card--front { left: 50px; top: 55px; }
  .card--back { left: 614px; top: 57px; }
  .card__art { position: absolute; inset: 0; }

  .holder { position: absolute; left: 47px; top: 50px; }
  .holder__name { font-size: 22px; font-weight: 700; letter-spacing: 0.2px; }
  .holder__role { margin-top: 22px; font-size: 13.5px; font-weight: 700; line-height: 20px; }
  .holder__contact { margin-top: 18px; font-size: 13.5px; font-weight: 700; line-height: 20px; }
  .holder__address { margin-top: 22px; font-size: 13.5px; font-weight: 700; line-height: 21px; }

  .company { position: absolute; left: 336px; width: 197px; top: 44px; text-align: center; color: #fff; }
  .company__name { font-size: 21px; font-weight: 700; line-height: 26px; }
  .company__tagline { margin-top: 10px; font-size: 10.5px; font-weight: 700; letter-spacing: 0.3px; }

  .brand { position: absolute; display: flex; flex-direction: column; align-items: center; text-align: center; }
  .brand__dot { width: 44px; height: 44px; border-radius: 50%; background: var(--red); }
  .brand__name { margin-top: 8px; font-size: 14px; font-weight: 700; line-height: 17px; color: var(--ink); }
  .card--front .brand { left: 373px; top: 172px; width: 120px; }
  .card--back .brand { left: 46px; top: 80px; width: 120px; }

  .phone { position: absolute; left: 36px; top: 234px; display: flex; align-items: center; gap: 8px; color: var(--red); font-size: 19px; font-weight: 700; }
  .phone svg { width: 15px; height: 15px; }

  .services { position: absolute; left: 254px; top: 26px; list-style: none; font-size: 14px; font-weight: 700; line-height: 15.5px; color: var(--charcoal); }
  .services li { position: relative; padding-left: 27px; }
  .services li::before { content: ""; position: absolute; left: 2px; top: 6px; width: 5px; height: 5px; border-radius: 50%; background: var(--red); }
</style>
</head>
<body>

<section class="card card--front">
  <svg class="card__art" width="533" height="307" viewBox="0 0 533 307" aria-hidden="true">
    <defs>
      <linearGradient id="front-fade" x1="0" y1="0" x2="0" y2="1">
        <stop offset="0" stop-color="#1e1e1e"/>
        <stop offset="0.35" stop-color="#3a3a3a"/>
        <stop offset="1" stop-color="#ffffff"/>
      </linearGradient>
    </defs>
    <rect x="336" y="0" width="197" height="260" fill="url(#front-fade)"/>
    <polygon points="294,0 336,0 336,68" fill="var(--red)"/>
  </svg>

  <div class="holder">
    <h1 class="holder__name">Dennis Holloway</h1>
    <p class="holder__role">Business Consultant / Project Manager<br>Experienced Builder (Dip Bdg &amp; Construction)</p>
    <p class="holder__contact">Mobile: 0481 362 954<br>E-mail: dennisholloway@harborconsulting.com.au</p>
    <p class="holder__address">PO Box 7814<br>Kelvin Heights, QLD,<br>4172 Australia</p>
  </div>

  <div class="company">
    <p class="company__name">Harbor Business<br>Consulting Pty Ltd</p>
    <p class="company__tagline">«BUILDING YOUR GOALS»</p>
  </div>

  <div class="brand">
    <span class="brand__dot"></span>
    <span class="brand__name">Harbor Business<br>Consulting</span>
  </div>
</section>

<section class="card card--back">
  <svg class="card__art" width="533" height="307" viewBox="0 0 533 307" aria-hidden="true">
    <defs>
      <linearGradient id="back-fade" x1="0" y1="0" x2="0" y2="1">
        <stop offset="0" stop-color="#1e1e1e"/>
        <stop offset="0.3" stop-color="#3a3a3a"/>
        <stop offset="1" stop-color="#ffffff"/>
      </linearGradient>
    </defs>
    <rect x="0" y="0" width="239" height="220" fill="url(#back-fade)"/>
    <polygon points="0,0 198,0 198,68 121,90 0,42" fill="#232323"/>
    <polygon points="198,68 239,0 198,0" fill="#232323"/>
    <polygon points="239,0 239,68 198,68" fill="var(--red)"/>
  </svg>

  <div class="brand">
    <span class="brand__dot"></span>
    <span class="brand__name">Harbor Business<br>Consulting</span>
  </div>

  <p class="phone">
    <svg viewBox="0 0 24 24" aria-hidden="true"><path fill="currentColor" d="M6.6 10.8a15.1 15.1 0 0 0 6.6 6.6l2.2-2.2a1 1 0 0 1 1-.25 11.4 11.4 0 0 0 3.6.57 1 1 0 0 1 1 1V20a1 1 0 0 1-1 1A17 17 0 0 1 3 4a1 1 0 0 1 1-1h3.5a1 1 0 0 1 1 1c0 1.25.2 2.45.57 3.57a1 1 0 0 1-.25 1z"/></svg>
    0481 362 954
  </p>

  <ul class="services">
    <li>Project Management</li>
    <li>Construction Design Advice/Mgmt</li>
    <li>Estimating Services<br>(Construction)</li>
    <li>Building Site Supervision</li>
    <li>Management of Building<br>Maintenance</li>
    <li>Site Relocations</li>
    <li>Subcontractor Management</li>
    <li>Medical /Health</li>
    <li>Commercial &amp; Industrial</li>
    <li>Retail/ Hospitality</li>
    <li>Community / Sports Facilities</li>
    <li>Educational Facilities</li>
    <li>Multi-Unit Residential</li>
    <li>Domestic</li>
  </ul>
</section>

</body>
</html>
```